Flyer-Design / Verodina
Zielgruppe
Licht zu verstehen und richtig einzusetzen ist ein wesentlicher Bestandteil, um die Wirkung von Architektur, Innenräumen und Landschaften zu unterstützen und zu steigern. Die harmonische Verschmelzung von moderner Architektur und akzentuiert eingesetztem Licht verleiht Innenräumen ihre eigene Note. Dieses Zusammenspiel erfordert über das Berechnen und die Leuchtenauswahl hinaus einen sehr sensiblen Umgang mit dem Medium Licht. Bei jeder Lichtplanung steht der Mensch mit seiner Wahrnehmung von Licht und Schatten im Mittelpunkt. Eine hochwertige Lichtplanung vom Fachmann verfolgt mit ihrem ganzheitlichen Ansatz daher den Anspruch Atmosphäre, Wohlbefinden und Orientierung zu schaffen und den beleuchteten Räumen Ausdruckskraft zu verleihen.
Aufgabenstellung
WIr möchten einen Flyer für unseren Laden der für den Kunden sehr ansprechend ist, im Bezug auf unserer Planungen und unseren Handel.
Wir möchten darauf eine Zusammenfassung unser Arbeit und unserer Portfolios sehen die dem Kunden sofort sagen was wir machen.

```html
<!DOCTYPE html>
<html lang="de">
<head>
<meta charset="utf-8">
<title>Verodina Flyer – Präsentation</title>
<link href="https://fonts.googleapis.com/css2?family=Questrial&family=Inter:wght@300;400&display=swap" rel="stylesheet">
<style>
  :root {
    --ink: #33363a;
    --sun: #fde400;
    --paper: #ffffff;
    --label: #222222;
    --muted: #b9bcbf;
  }
  * { margin: 0; padding: 0; box-sizing: border-box; }
  html, body { width: 1200px; height: 1200px; overflow: hidden; background: var(--paper); }
  .board { position: relative; width: 1200px; height: 1200px; font-family: "Inter", Helvetica, Arial, sans-serif; }

  .panel { position: absolute; background: var(--ink); overflow: hidden; box-shadow: 2px 3px 6px rgba(0,0,0,.35); }
  .panel svg.sun { position: absolute; left: 0; top: 0; }

  .outside { left: 257px; top: 23px; width: 702px; height: 351px; }
  .inside  { left: 257px; top: 408px; width: 702px; height: 351px; background: none; }
  .cover   { left: 261px; top: 810px; width: 347px; height: 353px; }
  .back    { left: 643px; top: 810px; width: 347px; height: 353px; }

  .brand { position: absolute; color: #fff; font-family: "Questrial", "Century Gothic", sans-serif; }
  .brand-name { font-size: 31px; letter-spacing: 5px; line-height: 1; white-space: nowrap; }
  .brand-tag { position: absolute; font-size: 9.5px; letter-spacing: 1.6px; line-height: 12px; color: var(--muted); white-space: nowrap; }

  .outside .brand { left: 402px; top: 62px; }
  .outside .brand-tag { left: 107px; top: 44px; }
  .cover .brand { left: 47px; top: 64px; }
  .cover .brand-tag { left: 105px; top: 42px; }

  .contact { position: absolute; font-size: 9.6px; line-height: 12.1px; color: var(--ink); font-weight: 400; }
  .contact p + p { margin-top: 12px; }
  .outside .contact { left: 212px; top: 216px; }
  .back .contact { left: 213px; top: 215px; }

  .claim-dark, .claim-light { position: absolute; font-size: 23.5px; font-weight: 300; line-height: 1; letter-spacing: -0.4px; white-space: nowrap; }
  .claim-dark { color: var(--ink); }
  .claim-light { color: #fff; }
  .outside .claim-dark { left: 401px; top: 301px; }
  .outside .claim-light { left: 540px; top: 301px; }
  .cover .claim-dark { left: 47px; top: 302px; }
  .cover .claim-light { left: 186px; top: 302px; }

  .grid { position: absolute; inset: 0; display: grid; grid-template-columns: repeat(4, 1fr); grid-template-rows: repeat(2, 1fr); box-shadow: 2px 3px 6px rgba(0,0,0,.35); }
  .cell { position: relative; }
  .cell-text { background: var(--ink); display: flex; align-items: center; justify-content: center; color: var(--sun); font-size: 9.8px; line-height: 12px; text-align: center; padding-bottom: 10px; }
  .photo-pendant { background: linear-gradient(180deg, #3a3a3c 0%, #2c2c2e 70%, #1b1b1c 100%); }
  .photo-ceiling { background: radial-gradient(ellipse at 50% 45%, #c9c9cc 0%, #9d9da1 55%, #d4d4d6 100%); }
  .photo-crystal { background: radial-gradient(ellipse at 50% 50%, #d8d8d8 0%, #f4f4f4 45%, #ffffff 70%); }
  .photo-wall { background: radial-gradient(ellipse at 45% 45%, #e9e9e9 0%, #cfcfcf 60%, #c4c4c4 100%); }
  .rule-h { position: absolute; left: 0; top: 174px; width: 351px; height: 2px; background: var(--sun); }
  .rule-v { position: absolute; left: 526px; top: 0; width: 2px; height: 351px; background: var(--sun); }

  .label { position: absolute; font-family: "Questrial", "Century Gothic", sans-serif; font-size: 25px; color: var(--label); line-height: 1; }
  .label-outside { left: 983px; top: 325px; }
  .label-inside  { left: 983px; top: 722px; }
  .label-cover   { left: 184px; top: 1120px; }
  .label-back    { left: 1021px; top: 1114px; }
</style>
</head>
<body>
<main class="board">

  <section class="panel outside" aria-label="Flyer außen">
    <svg class="sun" width="702" height="351" aria-hidden="true">
      <circle cx="349" cy="297" r="183" fill="var(--sun)"/>
      <line x1="349" y1="279" x2="532" y2="279" stroke="#ecd800" stroke-width="0.6"/>
    </svg>
    <div class="brand">
      <div class="brand-name">VERODINA</div>
      <div class="brand-tag">Lichtberatung +<br>Fachhandel</div>
    </div>
    <div class="contact">
      <p>verodina<br>Lindenhofweg 12<br>90482 Talbrunn<br>Tel: +49 9123-4567890<br>Email: info@verodina.de<br>www. verodina.de</p>
      <p>Öffnungszeiten:<br>(Mo–Fr.) 8:00–17:00</p>
    </div>
    <span class="claim-dark">wir machen</span>
    <span class="claim-light">licht</span>
  </section>
  <div class="label label-outside">aussen</div>

  <section class="panel inside" aria-label="Flyer innen">
    <div class="grid">
      <div class="cell photo-pendant" role="img" aria-label="Foto: schwarze Kuppel-Pendelleuchte über einem dunklen Tisch mit weißen Vasen"></div>
      <div class="cell cell-text">Lorem ipsum dolor sit amet,<br>consectetuer adipiscing elit.</div>
      <div class="cell photo-ceiling" role="img" aria-label="Foto: weiße zylindrische Deckenleuchte vor grauer Wand"></div>
      <div class="cell cell-text">Lorem ipsum dolor sit amet,<br>consectetuer adipiscing elit.</div>
      <div class="cell cell-text">Lorem ipsum dolor sit amet,<br>consectetuer adipiscing elit.</div>
      <div class="cell photo-crystal" role="img" aria-label="Foto: Kristall-Pendelleuchte auf weißem Grund"></div>
      <div class="cell cell-text">Lorem ipsum dolor sit amet,<br>consectetuer adipiscing elit.</div>
      <div class="cell photo-wall" role="img" aria-label="Foto: schwarze Wandleuchte mit goldener Innenseite"></div>
    </div>
    <div class="rule-h"></div>
    <div class="rule-v"></div>
  </section>
  <div class="label label-inside">innen</div>

  <section class="panel cover" aria-label="Flyer Titel">
    <svg class="sun" width="347" height="353" aria-hidden="true">
      <circle cx="0" cy="294" r="180" fill="var(--sun)"/>
      <line x1="0" y1="279" x2="178" y2="279" stroke="#ecd800" stroke-width="0.6"/>
    </svg>
    <div class="brand">
      <div class="brand-name">VERODINA</div>
      <div class="brand-tag">Lichtberatung +<br>Fachhandel</div>
    </div>
    <span class="claim-dark">wir machen</span>
    <span class="claim-light">licht</span>
  </section>
  <div class="label label-cover">Titel</div>

  <section class="panel back" aria-label="Flyer Rückseite">
    <svg class="sun" width="347" height="353" aria-hidden="true">
      <circle cx="347" cy="294" r="180" fill="var(--sun)"/>
    </svg>
    <div class="contact">
      <p>verodina<br>Lindenhofweg 12<br>90482 Talbrunn<br>Tel: +49 9123-4567890<br>Email: info@verodina.de<br>www. verodina.de</p>
      <p>Öffnungszeiten:<br>(Mo–Fr.) 8:00–17:00</p>
    </div>
  </section>
  <div class="label label-back">Rückseite</div>

</main>
</body>
</html>
```